Security Services Business Card

Looking for a clean modern style business card design for a residential and commercial security solutions provider. We install and service the following
security alarm, access control, video surveillance and fire alarm. Attached are the front and back of our current business cards in PSD file format.

Target Market(s)

Security alarm clients in the commercial and residential markets

Industry/Entity Type

Security Service

Contact Information for Business Card

We are open to designers suggestion and or design ideas.

Font styles to use
Serif
Sans Serif

Colors
3276b5
33a6d7
fffefd

Requirements
Must have
• Must have company logo , first and last name , phone number , web and email address, ect....

```html
<!DOCTYPE html>
<html lang="en">
<head>
<meta charset="utf-8">
<title>Vantora Security Systems – Business Card</title>
<link href="https://fonts.googleapis.com/css2?family=Roboto:wght@400;500;700&display=swap" rel="stylesheet">
<style>
  :root {
    --brand: #2878b8;
    --paper: #ffffff;
    --ink: #1b1b1b;
    --backdrop: #d3d3d3;
  }
  * { margin: 0; padding: 0; box-sizing: border-box; }
  html, body {
    width: 1200px; height: 1059px; overflow: hidden;
    background: var(--backdrop);
    font-family: "Roboto", Arial, sans-serif;
  }
  .canvas { position: relative; width: 1200px; height: 1059px; }

  .card {
    position: absolute;
    width: 690px; height: 392px;
    border-radius: 22px;
    overflow: hidden;
  }
  .card--front { left: 256px; top: 100px; background: var(--paper); }
  .card--back  { left: 254px; top: 537px; background: var(--brand); }

  .wordmark {
    position: absolute; left: 0; right: 0;
    text-align: center;
    font-weight: 700;
    letter-spacing: 0.5px;
    line-height: 1;
  }
  .card--front .wordmark { top: 100px; font-size: 44px; color: var(--brand); }
  .card--back  .wordmark { top: 170px; font-size: 54px; color: var(--paper); }

  .holder {
    position: absolute; right: 366px; top: 234px;
    text-align: right;
  }
  .holder__name {
    font-size: 24px; font-weight: 700; color: var(--brand);
    letter-spacing: 0.2px; line-height: 1;
  }
  .holder__title {
    margin-top: 7px;
    font-size: 16px; color: var(--ink); line-height: 1;
  }
  .divider {
    position: absolute; left: 344px; top: 229px;
    width: 1px; height: 57px; background: var(--brand);
  }
  .contacts {
    position: absolute; left: 366px; top: 224px;
    list-style: none;
  }
  .contacts li {
    display: flex; align-items: center; gap: 7px;
    height: 23.5px;
    font-size: 15.5px; color: var(--ink);
  }
  .contacts svg { width: 12px; height: 12px; fill: var(--brand); flex: none; }

  .address-band {
    position: absolute; left: 0; right: 0; top: 323px; height: 33px;
    background: var(--brand); color: var(--paper);
    font-size: 15.5px;
    display: flex; align-items: center; justify-content: center;
  }

  .services-heading {
    position: absolute; left: 0; right: 0; top: 296px;
    text-align: center; color: var(--paper);
    font-size: 18.5px; font-weight: 700; letter-spacing: 0.3px;
  }
  .services-rule {
    position: absolute; left: 217px; top: 328px;
    width: 258px; height: 1px; background: var(--paper);
  }
  .services-list {
    position: absolute; left: 0; right: 0; top: 340px;
    display: flex; justify-content: center; gap: 12px;
    list-style: none;
    color: var(--paper); font-size: 19.5px;
  }
  .services-list li::before { content: "•"; margin-right: 5px; font-size: 14px; vertical-align: 2px; }
</style>
</head>
<body>
<main class="canvas">

  <section class="card card--front" aria-label="Card front">
    <div class="wordmark">Vantora Security Systems</div>

    <div class="holder">
      <div class="holder__name">DANIEL REYES</div>
      <div class="holder__title">Owner/CEO</div>
    </div>
    <div class="divider"></div>

    <ul class="contacts">
      <li>
        <svg viewBox="0 0 24 24" aria-hidden="true"><path d="M6.6 10.8a15.2 15.2 0 0 0 6.6 6.6l2.2-2.2a1 1 0 0 1 1-.25 11.4 11.4 0 0 0 3.6.57 1 1 0 0 1 1 1V20a1 1 0 0 1-1 1A17 17 0 0 1 3 4a1 1 0 0 1 1-1h3.5a1 1 0 0 1 1 1c0 1.25.2 2.45.57 3.57a1 1 0 0 1-.25 1z"/></svg>
        555.204.7180 ext 106
      </li>
      <li>
        <svg viewBox="0 0 24 24" aria-hidden="true"><path d="M2 5h20v14H2z M3.5 6.5 12 13l8.5-6.5" stroke="#fff" stroke-width="1.5"/></svg>
        name@vantorainfo.com
      </li>
      <li>
        <svg viewBox="0 0 24 24" aria-hidden="true"><circle cx="12" cy="12" r="10"/><path d="M2 12h20M12 2c3 3 3 17 0 20M12 2c-3 3-3 17 0 20" stroke="#fff" stroke-width="1.4" fill="none"/></svg>
        www.vantorainfo.com
      </li>
    </ul>

    <div class="address-band">4720 Lakeview Ave # 310, Fairmont Ohio 44208</div>
  </section>

  <section class="card card--back" aria-label="Card back">
    <div class="wordmark">Vantora Security Systems</div>

    <h2 class="services-heading">WE INSTALL AND SERVICE</h2>
    <div class="services-rule"></div>
    <ul class="services-list">
      <li>Security Alarm</li>
      <li>Access Control</li>
      <li>Video Surveillance</li>
      <li>Fire Alarm</li>
    </ul>
  </section>

</main>
</body>
</html>
```